***PLASTIC*** Business Card Design

1 sided business card design
The card will be screen printed on plastic, so colour and fonts must be strong.

Must use the colours in the logo eps attached (Black/Ivory/White). Other colour(s) can be added.

Four (4) examples of how the logo can be printed are included in the logo eps attached.

The business card should highlight the logo. The card will be given to architects, interior designers and builders. It should look sophisticated but also innovative.

Do not cover the whole card with colour as it is important than some of the frosted plastic card is visible.

Be creative.

Target Market(s)

architects, interior designers and builders and wealthy home owners

Industry/Entity Type

Plastic

Requirements
Must have
• Must use the colours in the logo eps attached (Black/Ivory/White). Other colour(s) can be added if necessary.

The font is Square721 ExBT but has been a little thickened. It is not essential that you use this font. The name should be a stronger version of the font than other details.

The card will be printed on PVC - see http://www.voltrap.com.au/pricelistbcardsplastic.php

Final artwork must be print ready. You must use the printing spec at http://www.voltrap.com.au/2011%20PVC-TW.pdf

The actual details to be typeset ono the card are:

Dorian Welch

Mobile: 0412 806133
email: info@halcoworks.com.au
www.halcoworks.com.au

PO Box 53, Altona, Vic 3018

Plastering | Rendering | Cornicing

```html
<!DOCTYPE html>
<html lang="en">
<head>
<meta charset="utf-8">
<title>Halco Works – Business Card</title>
<link rel="stylesheet" href="https://fonts.googleapis.com/css2?family=Michroma&family=Jost:wght@400&display=swap">
<style>
  :root {
    --backdrop: #b3b3b3;
    --trim-line: #e0604a;
    --safe-line: #3a8fd0;
    --card-black: #000000;
    --ivory: #f7efd6;
    --white: #ffffff;
    --gold: #e3b420;
    --photo-light: #f2f0ea;
    --photo-orange: #d9733a;
    --photo-green: #6fa04a;
  }
  * { margin: 0; padding: 0; box-sizing: border-box; }
  html, body {
    width: 1200px;
    height: 773px;
    overflow: hidden;
    background: var(--backdrop);
  }
  .artboard {
    position: relative;
    width: 1200px;
    height: 773px;
  }
  .bleed-guide {
    position: absolute;
    left: 30px; top: 24px;
    width: 1147px; height: 721px;
    border: 1px solid var(--trim-line);
    border-radius: 20px;
  }
  .card {
    position: absolute;
    left: 53px; top: 46px;
    width: 1102px; height: 674px;
    background: var(--card-black);
    border: 1px solid var(--safe-line);
    border-radius: 16px;
    overflow: hidden;
  }
  .brand-name {
    position: absolute;
    left: 22px; top: 100px;
    font-family: "Michroma", sans-serif;
    font-size: 52px;
    line-height: 1;
    letter-spacing: 4px;
    color: var(--ivory);
    white-space: nowrap;
  }
  .contact-name {
    position: absolute;
    left: 34px; top: 416px;
    font-family: "Michroma", sans-serif;
    font-size: 25px;
    letter-spacing: 1px;
    color: var(--gold);
    white-space: nowrap;
  }
  .contact-details {
    position: absolute;
    left: 34px; top: 470px;
    font-family: "Michroma", sans-serif;
    font-size: 17px;
    line-height: 23px;
    letter-spacing: 1px;
    color: var(--white);
    white-space: nowrap;
  }
  .contact-details .postal { margin-top: 22px; }
  .services {
    position: absolute;
    left: 31px; top: 606px;
    font-family: "Jost", sans-serif;
    font-weight: 400;
    font-size: 40px;
    line-height: 1.1;
    letter-spacing: 1.5px;
    color: var(--white);
    white-space: nowrap;
  }
  .services .divider { margin: 0 14px; }
  .feature-image {
    position: absolute;
    left: 760px; top: 24px;
    width: 290px; height: 640px;
    clip-path: polygon(42% 0, 58% 0, 100% 100%, 0 100%);
    background: linear-gradient(160deg, var(--photo-light) 0%, var(--photo-orange) 45%, var(--photo-light) 65%, var(--photo-green) 85%, var(--photo-light) 100%);
  }
</style>
</head>
<body>
  <div class="artboard">
    <div class="bleed-guide"></div>
    <div class="card">
      <div class="brand-name">HALCO WORKS</div>

      <div class="contact-name">Dorian Welch</div>

      <div class="contact-details">
        <p>Mobile: 0412 806133</p>
        <p>email: info@halcoworks.com.au</p>
        <p>www.halcoworks.com.au</p>
        <p class="postal">PO Box 53, Brinsley, Vic 3990</p>
      </div>

      <div class="services">Plastering<span class="divider">|</span>Rendering<span class="divider">|</span>Cornicing</div>

      <div class="feature-image" role="img" aria-label="Photograph of a tall house of playing cards stacked in tiers"></div>
    </div>
  </div>
</body>
</html>
```